Personal coach needs brochure design for inspirational essay about authenticity

Overview:
I want a beautiful brochure, 11”x17” that folds to 8-1/2”x11” with 4 pages. Think of it as an oversize greeting card.
• Front cover: photograph of a dancer and title with attribution of quote (Lumafold jpeg photo attached)
• Inside spread: Copy (Helena Brisk copy attached) with some appropriate illustration, based on cover photo
• Back cover: contact information, brief descriptive copy, two small photos (jpeg photo attached; see copy for direction)
Copy for front cover title, inside spread and back cover is attached in doc titled "Helena Brisk copy"

Purpose of brochure:
I'm a personal coach and once a year I produce a 4-page illustrated inspirational essay, which invites personal reflection on living a more mindful, meaningful life. Most people I send them to collect them. Someday in the future I'd like to put a collection of these essays into a coffee table book and also create a website for the collection, which is related to the personal coaching that I do.
I have the brochures printed hard copy. I have attached a few examples from previous years. Each has a unique design related to its theme.

Concept:
This year’s essay theme, “There will only ever be one you!” is based on a quote by Helena Brisk, a famous modern dancer. The complete quote, which appears in the copy, is about being true to one’s authentic self. The essay is not about dance, but because the author of the quote was a dancer who personified this theme of being unique to self, I have selected a photo of dance for the cover.

Design Guidance:
Front cover: One possibility is to expand the background color of the Lumafold photo so the photo seems to emerge from the background. But I am open to ideas. I think the photo is artsy enough as it is, but there may be other ways to treat it (e.g. special effects) that would also work. The title should appear somewhere. Make the attribution (--Helena Brisk) in smaller type than the title.

Inside Spread: There may be ways to borrow a design motif from the cover photo to make the inside spread more visually interesting, i.e., not just straight copy. I think it may be helpful to make the font size of the quote larger than the rest of the copy, but it has to be read in sequence. Or maybe it's printed in same size as copy, but then also repeated and displayed by itself in larger type.

Back cover: If you look at some of the other examples I’ve sent, you’ll see how the back cover is typically handled. I want a reduced version of the cover to be placed near the line that says "this is the 16th in a series.." Then, there’s a jpeg photo of Helena Brisk that should be placed next to the copy description of her.

Need extra days to review

```html
<!DOCTYPE html>
<html lang="en">
<head>
<meta charset="utf-8">
<title>There Will Only Ever Be One You – Brochure</title>
<link rel="stylesheet" href="https://fonts.googleapis.com/css2?family=Cinzel:wght@400&family=Merriweather:wght@300;700&family=Open+Sans:ital,wght@0,400;0,600;0,700;1,600;1,700&family=Sacramento&display=swap">
<style>
:root{
  --ink:#1c1c1c;
  --navy:#17233a;
  --cream:#f6ecd9;
  --smoke:#3a4247;
  --smoke-deep:#1d2326;
  --amber:#d99a2b;
  --sand:#d6b88a;
  --teal:#6f8c90;
  --white:#ffffff;
}
*{margin:0;padding:0;box-sizing:border-box}
html,body{width:838px;height:1200px;overflow:hidden;background:var(--white)}
body{position:relative;font-family:"Open Sans",sans-serif;color:var(--ink)}

.spread{position:absolute;left:63px;width:725px;height:469px;overflow:hidden}
.spread--outer{top:98px;
  background:
    radial-gradient(ellipse 30% 22% at 42% 92%, rgba(222,170,105,.8), transparent 70%),
    radial-gradient(ellipse 22% 18% at 25% 96%, rgba(120,150,150,.6), transparent 70%),
    radial-gradient(ellipse 28% 20% at 60% 82%, rgba(230,200,190,.55), transparent 70%),
    radial-gradient(ellipse 25% 15% at 8% 96%, rgba(200,150,95,.7), transparent 70%),
    linear-gradient(165deg,var(--smoke-deep) 0%,var(--smoke) 24%,#74797a 42%,#d9ccb6 62%,var(--cream) 100%);}
.spread--inner{top:628px;
  background:
    radial-gradient(ellipse 30% 22% at 22% 96%, rgba(205,145,80,.85), transparent 70%),
    radial-gradient(ellipse 28% 20% at 45% 90%, rgba(120,150,150,.6), transparent 70%),
    radial-gradient(ellipse 30% 25% at 80% 98%, rgba(60,80,85,.85), transparent 70%),
    radial-gradient(ellipse 25% 18% at 5% 85%, rgba(225,190,140,.8), transparent 70%),
    linear-gradient(180deg,#fbf4e4 0%,#f7ecd6 50%,#ecd7b0 68%,#b8a488 85%,#7b7a70 100%);}

/* ---------- back cover ---------- */
.back-photo{position:absolute;left:0;top:0;width:220px;height:260px;
  background:radial-gradient(ellipse 60% 55% at 45% 40%,#5c6569,#2a3033 70%,rgba(42,48,51,0) 100%)}
.back-arc{position:absolute;left:-48px;top:233px;width:440px;height:360px;border-radius:50%;
  background:radial-gradient(ellipse at 50% 20%,rgba(247,239,224,.95),rgba(240,226,200,.7) 70%,rgba(230,205,165,.4))}
.portrait{position:absolute;left:13px;top:168px;width:117px;height:117px;border-radius:50%;
  background:radial-gradient(circle at 50% 55%,#c9c0b2,#6b645c 45%,#1e1c1b 80%);border:1.5px solid var(--cream)}
.intro{position:absolute;left:203px;top:58px;width:160px;color:var(--white)}
.intro h2{font-family:"Merriweather",serif;font-weight:700;font-size:8.6px;margin-bottom:9px}
.intro p{font-size:5.8px;line-height:1.32;margin-bottom:8px;color:#e6e6e6;width:135px}
.contact{font-size:5.8px;line-height:1.3;color:#e6e6e6}
.contact strong{font-weight:700;color:var(--white)}
.contact li{list-style:none;display:flex;gap:4px;align-items:flex-start}
.contact svg{width:5px;height:6px;flex:none;margin-top:1px;fill:#e6e6e6}
.contact .indent{padding-left:9px}
.copyright{font-size:5.8px;margin-top:8px;color:#e6e6e6}
.about{position:absolute;left:14px;font-size:5.9px;line-height:1.32;color:#2a2a2a}
.about--dancer{top:262px;width:275px}
.about--photographer{top:370px;width:292px}
.about .label{font-weight:600;font-size:6.1px}
.about .name{font-family:"Sacramento",cursive;font-size:14px;line-height:1;margin:0 0 6px}
.about--dancer .label,.about--dancer .name{margin-left:112px}

/* ---------- front cover ---------- */
.cover-ring{position:absolute;left:418px;top:-8px;width:340px;height:340px;border-radius:50%;
  background:rgba(214,198,170,.55)}
.cover-photo{position:absolute;left:435px;top:15px;width:294px;height:294px;border-radius:50%;
  background:radial-gradient(circle at 55% 40%,#6b7478,#394146 40%,#14181a 78%)}
.title{position:absolute;left:400px;top:358px;width:300px;text-align:center;font-weight:400}
.title .script{font-family:"Sacramento",cursive;font-size:31px;line-height:1;display:block;color:#1a1a1a}
.title .big{font-family:"Cinzel",serif;font-size:36px;line-height:1.1;display:block;color:var(--navy)}
.title .attrib{font-style:italic;font-weight:600;font-size:9.5px;display:block;margin-top:8px;color:#1a1a1a}

/* ---------- inside spread ---------- */
.essay{position:absolute;left:34px;top:33px;width:301px;font-size:6.9px;line-height:9.2px;color:#222;text-align:justify}
.essay p{margin-bottom:9px}
.essay .pull{font-style:italic;font-weight:700;border-top:1.2px dotted var(--amber);border-bottom:1.2px dotted var(--amber);
  padding:11px 0;margin:12px 0 18px}
.quote{position:absolute;left:389px;top:30px;width:200px;font-family:"Merriweather",serif;font-weight:300;font-size:9.8px;line-height:11.9px;color:#1d1d1d}
.quote p{margin-bottom:11.9px}
.collage{position:absolute;left:555px;top:25px;width:160px;height:180px;
  background:
    radial-gradient(ellipse 38% 30% at 55% 62%, rgba(217,154,43,.75), transparent 72%),
    radial-gradient(ellipse 22% 20% at 65% 82%, rgba(120,120,120,.55), transparent 72%),
    radial-gradient(ellipse 30% 25% at 60% 22%, rgba(160,160,160,.35), transparent 72%)}
.reflection{position:absolute;left:387px;top:323px;width:327px;height:120px;border:1px solid rgba(255,255,255,.85);
  background:rgba(52,60,64,.72);color:#f2f2f2;font-size:6.6px;line-height:9.2px;text-align:center;padding:11px 18px}
.reflection p{margin-bottom:9px}
</style>
</head>
<body>

<section class="spread spread--outer" aria-label="Outer spread: back and front cover">
  <div class="back-photo" role="img" aria-label="Dancer leaping in a flowing dark dress against smoky grey"></div>
  <div class="back-arc"></div>
  <div class="portrait" role="img" aria-label="Archival black and white photograph of Helena Brisk dancing"></div>

  <div class="intro">
    <h2>There Will Only Ever Be One You</h2>
    <p>is the 16th in a series of Labor Day essays inviting a moment of reflection on living a more meaningful, more mindful life</p>
    <ul class="contact">
      <li class="indent"><strong>Nora Ellison Vale, Ph.D.</strong></li>
      <li><svg viewBox="0 0 10 12"><path d="M5 0a4 4 0 0 1 4 4c0 3-4 8-4 8S1 7 1 4a4 4 0 0 1 4-4zm0 2.5a1.5 1.5 0 1 0 0 3 1.5 1.5 0 0 0 0-3z"/></svg>Heron Hill House</li>
      <li class="indent">18 Orchard Lane, Millbrook,</li>
      <li class="indent">Vermont&nbsp; 05601</li>
      <li><svg viewBox="0 0 10 12"><rect x="2" y="0" width="6" height="12" rx="1"/></svg>Mobile:&nbsp; 555-013-2840</li>
      <li><svg viewBox="0 0 10 12"><rect x="0" y="3" width="10" height="7"/></svg>nvale@example.com</li>
    </ul>
    <p class="copyright">©2023</p>
  </div>

  <div class="about about--dancer">
    <div class="label">ABOUT</div>
    <div class="name">Helena Brisk:</div>
    <p>Born in 1894, Helena Brisk danced and taught for over 70 years. She is recognized as a primal artistic force of the 20th century, whose influence on modernity has been compared to Varenne, Tobias Wren, Kovalenko, and Elias Marsh. Her themes dealt with the lives and conflicts of ordinary people, and she brought serious issues to the stage like war, poverty, intolerance and the injustices of slavery and treatment of Native Americans. Rebelling against conventions of the past, her dancing and choreography exposed the depths of human emotion through intense movements that were forceful, stark, angular, jagged, and percussive – startlingly unlike the formality of classical ballet, which she saw as antiquated.</p>
  </div>
  <div class="about about--photographer">
    <div class="label">ABOUT PHOTOGRAPHER</div>
    <div class="name">Iris Calloway:</div>
    <p>In 1935 Iris Calloway saw a performance by modern dancer and choreographer Helena Brisk. Calloway was so inspired by the dance performance that she introduced herself to Brisk, and the two artists began an artistic collaboration that lasted more than 60 years. Calloway often photographed dancers in action, to capture the emotion behind their movement. Her artistic style was in line with Brisk's philosophy of dance. This photo from the dance, "Letter to the World," is one of Calloway's most famous photographs. The title of this work comes from a Clara Whitcombe poem, which inspired Brisk to create a dance performance based on Whitcombe's life.</p>
  </div>

  <div class="cover-ring"></div>
  <div class="cover-photo" role="img" aria-label="Dancer in mid-leap, dark dress and dust against a black background"></div>
  <h1 class="title">
    <span class="script">There will only ever be</span>
    <span class="big">ONE YOU!</span>
    <span class="attrib">Helena&nbsp; Brisk</span>
  </h1>
</section>

<section class="spread spread--inner" aria-label="Inside spread: essay">
  <div class="essay">
    <p>In the rural Ohio village where I grew up, one of the highlights of Sunday morning church service -- in between congregational hymn-singing and the preacher's sermon -- was the "special selection," a musical performance by a parishioner. Typically, it was a vocalist or instrumental on piano, organ or violin. One Sunday, we were surprised by an unusual performance. A plump, buxom farm wife approached the pulpit, puckered up her lips and unexpectedly began to whistle the hymn "The Old Rugged Cross." As a 10-year-old, I found this hilarious as I tried to choke back my wide-eyed amazement and giggles.</p>
    <p class="pull">Despite the irreverence of my pre-adolescent reaction, this memory has stayed with me for decades as an iconic example of the wonderment of individual differences. Of the delight I find in witnessing someone express herself in sometimes surprising and even courageous ways. Of the marvel of beholding a person be truly authentic and uniquely original.</p>
    <p>Someone who personified the irrepressible impulse to express her individuality was the early 20th century dancer and choreographer Helena Brisk. A pioneer of modern dance, she threw tradition overboard and was inspired to dance in a way that was a radical departure from the formalized style and rigidly dictated forms of classical ballet. Brisk felt compelled to express the rawness and emotion of human experience in her dancing -- not just present a form of pretty entertainment. Iconoclastically brilliant, she created a new language of dance, a revolutionary vocabulary of movement that electrified the stage, often creating a visceral response in the audience.</p>
    <p>In her biography of Brisk, her friend and equally talented choreographer Ruth Ambler recalled that despite sensational reviews for her own innovative work in the Broadway musical Prairie Song!, Ambler had a gnawing feeling that her work was only mediocre. Ambler confessed her anxieties to Brisk who listened quietly and then responded, "There will only ever be one you!" Continuing, she added:</p>
  </div>

  <div class="quote">
    <p>“There is a vitality,<br>a life-force, an energy,<br>a quickening that is translated<br>through you into action.</p>
    <p>And because there is only<br>one of you in all of time,<br>this expression is unique.<br>And if you block it,<br>the world will not have it.</p>
    <p>It is not your business<br>to determine<br>how good it is nor how valuable<br>nor how it compares<br>with other expressions.<br>It is your business to keep it yours<br>clearly and directly,<br>to keep the channel open.</p>
    <p>You have to keep open and aware<br>directly to the urges that motivate you.<br>Above all else, keep the channel open!”</p>
  </div>

  <div class="collage" role="img" aria-label="Collage illustration: a ballerina balancing on the moon among planets and constellations, with an amber triangle"></div>

  <div class="reflection">
    <p>Brisk's wisdom reminds us that we must not hold back or judge our gifts. Although there may be moments when we doubt ourselves or when we worry that we're not good enough, our job is to be fearless and to "keep the channel open."</p>
    <p>Guard the precious miracle of your own uniqueness.<br>Find that home-sweet-home feeling where you feel you are your most authentic self. There will only ever be one you! And importantly, respect the differences of others. Our world would be a drab, boring place if we all only whistled one tune.</p>
  </div>
</section>

</body>
</html>
```